MORVANE GROUP (STATIONARY)
MORVANE CONSULTING GROUP, LLC
Please update design to show my name next to the Title, Principal : Delbert T. Worrow III
Also, please fix the address in the design :
4827 Halvorsen St. NW, Washington, DC 20374
Last, I am also looking for other stationary such as letterhead , letters and invoices. (not just the business card)
Thank you!
Delbert

```html
<!DOCTYPE html>
<html lang="en">
<head>
<meta charset="utf-8">
<title>Morvane Group — Stationery Set</title>
<link href="https://fonts.googleapis.com/css2?family=Montserrat:wght@400;600&display=swap" rel="stylesheet">
<style>
  :root{
    --stage:#3b3b3d;
    --paper:#ffffff;
    --paper-shade:#e9e9ea;
    --envelope-back:#9a9a9c;
    --ink:#4a4a4c;
    --ink-soft:#8c8c8f;
    --brand:#d93a74;
    --brand-faint:rgba(217,58,116,.08);
    --card-dark:#2a2a2c;
    --white:#ffffff;
  }
  *{box-sizing:border-box;margin:0;padding:0}
  html,body{width:1200px;height:310px;overflow:hidden}
  body{background:var(--stage);font-family:"Montserrat",Arial,sans-serif;color:var(--ink);position:relative}
  .piece{position:absolute;background:var(--paper);box-shadow:0 1px 3px rgba(0,0,0,.45)}

  .brand{display:flex;align-items:center;gap:6px}
  .brand-dot{border-radius:50%;background:var(--brand);flex:none}
  .brand-name{font-weight:600;letter-spacing:.06em;line-height:1.05;color:var(--brand)}

  /* hero logo on stage */
  .hero{position:absolute;left:66px;top:62px}
  .hero .brand-dot{width:34px;height:34px}
  .hero .brand-name{font-size:21px;color:var(--white)}
  .hero-tag{font-size:7px;color:var(--brand);margin:4px 0 0 40px;letter-spacing:.05em}

  /* business cards */
  .card-detail{left:72px;top:166px;width:118px;height:66px;padding:8px}
  .card-detail .brand-dot{width:12px;height:12px}
  .card-detail .brand-name{font-size:7px}
  .card-detail .contact{margin-top:8px;font-size:4px;line-height:1.45;color:var(--ink-soft)}
  .card-detail .contact strong{color:var(--ink);font-weight:600}
  .card-front{left:19px;top:256px;width:96px;height:44px;display:flex;align-items:center;justify-content:center}
  .card-front .brand-dot{width:14px;height:14px}
  .card-front .brand-name{font-size:7px}
  .card-back{left:132px;top:256px;width:84px;height:44px;background:var(--card-dark);display:flex;align-items:center;justify-content:center}
  .card-back .brand-dot{width:14px;height:14px}
  .card-back .brand-name{font-size:6.5px;color:var(--white)}

  /* letterheads */
  .letterhead{top:18px;width:144px;height:272px;padding:10px 12px}
  .letterhead-a{left:283px}
  .letterhead-b{left:456px}
  .letterhead .brand-dot{width:12px;height:12px}
  .letterhead .brand-name{font-size:6px}
  .letterhead .header-contact{position:absolute;right:12px;top:10px;font-size:3.4px;line-height:1.5;color:var(--ink-soft);text-align:right}
  .letterhead .faint-mark{position:absolute;left:32px;top:86px;width:80px;height:80px;border-radius:50%;background:var(--brand-faint)}
  .letterhead .footer{position:absolute;left:0;right:0;bottom:8px;font-size:3.4px;text-align:center;color:var(--ink-soft)}

  /* compliment slips */
  .slip{left:696px;width:132px;height:72px;padding:8px}
  .slip-top{top:84px}
  .slip-bottom{top:180px}
  .slip .brand-dot{width:10px;height:10px}
  .slip .brand-name{font-size:5.5px}
  .slip .footer{position:absolute;left:0;right:0;bottom:5px;font-size:3.2px;text-align:center;color:var(--ink-soft)}

  /* envelopes */
  .envelope{left:852px;width:156px}
  .envelope svg{position:absolute;inset:0}
  .envelope-back{top:60px;height:48px;background:var(--envelope-back)}
  .envelope-flap{top:113px;height:79px}
  .envelope-front{top:197px;height:67px;padding:8px}
  .envelope .brand-dot{width:10px;height:10px}
  .envelope .brand-name{font-size:5.5px}
  .envelope-flap .brand{position:absolute;left:62px;top:40px}
</style>
</head>
<body>

  <div class="hero">
    <div class="brand"><span class="brand-dot"></span><span class="brand-name">MORVANE<br>GROUP</span></div>
    <p class="hero-tag">Business Concepts</p>
  </div>

  <div class="piece card-detail">
    <div class="brand"><span class="brand-dot"></span><span class="brand-name">MORVANE GROUP</span></div>
    <p class="contact"><strong>Delbert T. Worrow III</strong> · Principal<br>4827 Halvorsen St. NW<br>Washington, DC 20374<br>202.555.0148</p>
  </div>
  <div class="piece card-front">
    <div class="brand"><span class="brand-dot"></span><span class="brand-name">MORVANE GROUP</span></div>
  </div>
  <div class="piece card-back">
    <div class="brand"><span class="brand-dot"></span><span class="brand-name">MORVANE GROUP</span></div>
  </div>

  <div class="piece letterhead letterhead-a">
    <div class="brand"><span class="brand-dot"></span><span class="brand-name">MORVANE<br>GROUP</span></div>
    <p class="header-contact">4827 Halvorsen St. NW<br>Washington, DC 20374<br>202.555.0148</p>
    <span class="faint-mark"></span>
    <p class="footer">MORVANE CONSULTING GROUP, LLC · morvaneconsulting.com</p>
  </div>
  <div class="piece letterhead letterhead-b">
    <div class="brand"><span class="brand-dot"></span><span class="brand-name">MORVANE<br>GROUP</span></div>
    <span class="faint-mark"></span>
    <p class="footer">4827 Halvorsen St. NW, Washington, DC 20374 · 202.555.0148</p>
  </div>

  <div class="piece slip slip-top">
    <div class="brand"><span class="brand-dot"></span><span class="brand-name">MORVANE<br>GROUP</span></div>
    <p class="footer">4827 Halvorsen St. NW, Washington, DC 20374</p>
  </div>
  <div class="piece slip slip-bottom">
    <div class="brand"><span class="brand-dot"></span><span class="brand-name">MORVANE<br>GROUP</span></div>
    <p class="footer">4827 Halvorsen St. NW, Washington, DC 20374</p>
  </div>

  <div class="piece envelope envelope-back">
    <svg viewBox="0 0 156 48" width="156" height="48"><polyline points="0,0 78,30 156,0" fill="none" stroke="#b8b8ba" stroke-width="1"/></svg>
  </div>
  <div class="piece envelope envelope-flap">
    <svg viewBox="0 0 156 79" width="156" height="79"><polygon points="0,0 78,34 156,0" fill="var(--paper-shade)"/><polyline points="0,79 62,36 M156,79 94,36" fill="none" stroke="#dadadc" stroke-width="1"/></svg>
    <div class="brand"><span class="brand-dot"></span><span class="brand-name">MORVANE<br>GROUP</span></div>
  </div>
  <div class="piece envelope envelope-front">
    <div class="brand"><span class="brand-dot"></span><span class="brand-name">MORVANE<br>GROUP</span></div>
  </div>

</body>
</html>
```